New Template, new corporate image Quelmoro 2022

New template designs for google slides or PowerPoint. Match to new corporate image. The new website www.quelmoro-mx.com Needs to match our new version. Technology and Artificial Intelligence elements to reflect our type of work.
We are adding old version of template and will send elements for the new corporate images.
Please consider our website as the main corporate image.
Our templates are being used on customer presentations, webminars, internal work only.
We have our main name of company Quelmoro. Quelmoro has to be in all the templates.
Secondary logo or branded service is: Calvindar.

Target Market(s)

Industrial users. Asset managers. Corporate visitors and customers.

Industry/Entity Type

Automotive. Chemical. Food and Beverage. Manufacturing

Other font styles liked:
• Norvex INSPIRA. RALEWAY

Colors
0054AA
0677BA
7BADD7
CADEEF
E8F1F8

Requirements
Must have
• Match to our elements on the new image. Use Brain Icons. Chips icons to connect equipments with software and control. Innovation.
Nice to have
• Unique images, machine images. Connecting machines and data elements. Template version for google slides. Image for industrial software for control equipment and saving money to manufacturers. Segments: Automotive, Chemical, Food and Beverages, Mining and pharmaceutical, Energy Management
Should not have
• old elements. not to much images of medical devices. Do not seems like a hospital.

```html
<!DOCTYPE html>
<html lang="en">
<head>
<meta charset="utf-8">
<title>Quelmoro Template 2022</title>
<link href="https://fonts.googleapis.com/css2?family=Open+Sans:wght@400;600;700;800&display=swap" rel="stylesheet">
<style>
:root{
  --blue:#0d3fa6;
  --blue-deep:#0a2f86;
  --blue-bright:#1f3fd8;
  --red:#f2232f;
  --grey-bg:#a8a9ab;
  --ink:#1b1b1b;
  --body:#3a3a3a;
  --number:#c9c9c9;
  --white:#ffffff;
}
*{margin:0;padding:0;box-sizing:border-box}
html,body{width:1200px;height:3375px;overflow:hidden}
body{position:relative;background:var(--grey-bg);font-family:"Open Sans",Arial,sans-serif;color:var(--ink)}
.backdrop{position:absolute;inset:0;width:1200px;height:3375px}
.slide{position:absolute;left:100px;width:1000px;height:563px;background:var(--white);overflow:hidden;box-shadow:0 4px 14px rgba(0,0,0,.18)}
.abs{position:absolute}
.brand{position:absolute;right:30px;top:22px;font-size:19px;font-weight:600;color:var(--blue);letter-spacing:.3px}
.dots{position:absolute;left:32px;top:18px;display:flex;gap:6px}
.dots i{width:9px;height:9px;border-radius:50%;background:var(--red)}
.dots i+i{background:var(--blue)}
.heading{position:absolute;left:30px;top:32px;font-size:26px;font-weight:700;letter-spacing:.3px;color:var(--ink)}
.social{position:absolute;left:32px;display:flex;gap:4px}
.social i{width:18px;height:18px;border-radius:50%;background:var(--blue)}
.social i:nth-child(2){background:#3a8de0}
.social i:nth-child(3){background:var(--red)}
.page{position:absolute;right:30px;width:28px;height:28px;border-radius:50%;background:var(--blue-bright);color:#fff;font-size:14px;font-weight:700;display:flex;align-items:center;justify-content:center}

/* cover */
.cover-top{position:absolute;left:0;top:0;width:1000px;height:63px;background:#fff}
.cover-top .brand{left:0;right:0;text-align:center;top:18px}
.cover-rule{position:absolute;left:0;top:63px;width:1000px;height:4px;background:var(--red)}
.cover-image{position:absolute;left:0;top:67px;width:1000px;height:496px;background:radial-gradient(ellipse at 35% 45%,#2a62c9 0%,#1446a8 45%,#0a2a78 100%)}
.cover-text{position:absolute;left:0;width:1000px;text-align:center;color:#fff}
.cover-title{top:170px;font-size:26px;font-weight:700;letter-spacing:.5px}
.cover-sub{top:222px;font-size:27px;font-weight:700;line-height:41px;letter-spacing:.3px}
.cover-tag{top:328px;font-size:10px;font-weight:700;letter-spacing:4px}
.cover-date{top:352px;font-size:10px;font-weight:700;letter-spacing:4px}
.cover .social{left:470px;top:501px}
.cover .page{background:#fff;color:var(--ink)}

/* services */
.service{position:absolute;width:380px}
.service .num{position:absolute;left:0;top:-4px;font-size:50px;font-weight:600;color:var(--number);line-height:1}
.service h3{position:absolute;left:52px;top:0;font-size:16px;font-weight:700;color:var(--blue)}
.service p{position:absolute;left:52px;top:28px;width:370px;font-size:10.5px;line-height:15.5px;color:var(--body)}

/* industries */
.industry-dot{position:absolute;width:54px;height:54px;border-radius:50%;background:var(--blue);box-shadow:0 3px 8px rgba(13,63,166,.35)}
.industry-label{position:absolute;font-size:10.5px;font-weight:700;color:var(--ink)}

/* who we are */
.who-copy{position:absolute;left:32px;width:454px;font-size:10.5px;line-height:15.5px;color:var(--body);text-align:justify}
.who-sub{position:absolute;left:31px;font-size:22px;font-weight:700;color:var(--blue)}

/* allies */
.ally{position:absolute;border-radius:50%;background:#ececec;display:flex;align-items:center;justify-content:center;font-size:19px;font-weight:600;color:#333}
.ally b{display:inline-block;width:12px;height:12px;background:var(--blue);margin-right:8px}
.allies-copy{position:absolute;left:519px;top:102px;width:452px;font-size:10.3px;line-height:15.5px;color:var(--body);text-align:justify}
.allies-copy p{margin-bottom:15px}
</style>
</head>
<body>

<svg class="backdrop" viewBox="0 0 1200 3375" aria-hidden="true">
  <polygon points="1200,1107 1200,3375 0,3375 0,2345" fill="#0d3fa6"/>
</svg>

<!-- Slide 1: cover -->
<section class="slide cover" style="top:124px">
  <div class="cover-top"><div class="brand">Quelmoro</div></div>
  <div class="cover-rule"></div>
  <div class="cover-image" role="img" aria-label="Blue technology scene: a hand touching a network of connected industrial icons"></div>
  <div class="cover-text cover-title">INDUSTRIAL DATA HUB</div>
  <div class="cover-text cover-sub">UNIVERSAL ACCESS TO CORRECT DATA, ORDERED BY<br>TIME. CORVANE PREFERRED DISTRIBUTOR</div>
  <div class="cover-text cover-tag">LOREM IPSUM DOLOR SIT AMET</div>
  <div class="cover-text cover-date">JULY 2021</div>
  <div class="social"><i></i><i></i><i></i></div>
  <div class="page" style="top:516px">1</div>
</section>

<!-- Slide 2: services -->
<section class="slide" style="top:768px">
  <div class="dots"><i></i><i></i></div>
  <div class="heading">OUR SERVICES</div>
  <div class="brand">Quelmoro</div>

  <div class="service" style="left:62px;top:107px"><span class="num">1</span><h3>TECH SUPPORT</h3>
    <p>At Quelmoro we are committed to providing the best service to our clients, for that reason we make sure that each case is resolved quickly and efficiently.</p></div>
  <div class="service" style="left:62px;top:250px"><span class="num">2</span><h3>CERTIFICATION</h3>
    <p>We offer official certifications, as well as fully-customized courses based on the unique need of each client. Quelmoro is a training center for Norvex and Corvane in Mexico.</p></div>
  <div class="service" style="left:62px;top:394px"><span class="num">3</span><h3>TECH COURSES</h3>
    <p>We offer completely customized courses based on the need of our customers. We have several training centers in the Mexican Republic.</p></div>
  <div class="service" style="left:531px;top:107px"><span class="num">4</span><h3>DIAGNOSTICS</h3>
    <p>We offer the most advanced in industrial technology, Hardware and Software update. Learn about our success stories and discover the benefits of updating your equipment.</p></div>
  <div class="service" style="left:531px;top:250px"><span class="num">5</span><h3>CONSULTORY</h3>
    <p>The Projects program was developed to enrich and extend the useful life of your software and hardware. Combine software updates and updates with technical support services.</p></div>
  <div class="service" style="left:531px;top:394px"><span class="num">6</span><h3>CUSTOMER ATTENTION</h3>
    <p>We provide solutions to events that may affect the optimal operation of your plant. Remotely, our team of engineers can assist you in the remote resolution of high-urgency events anywhere in the world, as well as remote software review.</p></div>

  <div class="social" style="top:518px"><i></i><i></i><i></i></div>
  <div class="page" style="top:514px">2</div>
</section>

<!-- Slide 3: industries -->
<section class="slide" style="top:1410px">
  <div class="dots"><i></i><i></i></div>
  <div class="heading">INDUSTRIES WE SERVE</div>
  <div class="brand">Quelmoro</div>

  <div class="abs" style="left:106px;top:132px;width:52px;height:184px;background:var(--blue)"></div>
  <div class="abs" style="left:255px;top:448px;width:185px;height:47px;background:var(--red)"></div>
  <div class="abs" role="img" aria-label="Photo of a laptop showing machine data held in front of a factory line" style="left:159px;top:102px;width:398px;height:346px;background:linear-gradient(135deg,#d8c2a8 0%,#9aa0a6 45%,#5c6470 75%,#2b2f36 100%)"></div>

  <svg class="abs" style="left:0;top:0" width="1000" height="563" aria-hidden="true">
    <g fill="none" stroke="#555" stroke-width="1" stroke-dasharray="3 3">
      <path d="M644 175 Q690 185 717 193"/>
      <path d="M717 247 Q680 262 644 264"/>
      <path d="M644 318 Q690 330 717 336"/>
      <path d="M717 390 Q680 402 644 407"/>
    </g>
    <g fill="none" stroke="#fff" stroke-width="1.6">
      <rect x="633" y="139" width="22" height="16" rx="2"/><line x1="637" y1="145" x2="651" y2="145"/>
      <circle cx="717" cy="220" r="8"/><circle cx="717" cy="220" r="3"/>
      <circle cx="644" cy="287" r="7"/><path d="M635 302 q9 -10 18 0"/>
      <path d="M707 372 v-18 h8 v8 h12 v10 z"/>
      <path d="M633 440 a11 11 0 0 1 22 0 z"/><line x1="630" y1="440" x2="658" y2="440"/>
    </g>
  </svg>
  <div class="industry-dot" style="left:617px;top:121px"></div>
  <div class="industry-dot" style="left:690px;top:193px"></div>
  <div class="industry-dot" style="left:617px;top:264px"></div>
  <div class="industry-dot" style="left:690px;top:336px"></div>
  <div class="industry-dot" style="left:617px;top:407px"></div>
  <svg class="abs" style="left:0;top:0" width="1000" height="563" aria-hidden="true">
    <g fill="none" stroke="#fff" stroke-width="1.6">
      <rect x="633" y="140" width="22" height="16" rx="2"/><line x1="637" y1="146" x2="651" y2="146"/><line x1="637" y1="151" x2="647" y2="151"/>
      <circle cx="717" cy="220" r="9"/><circle cx="717" cy="220" r="3"/>
      <circle cx="644" cy="286" r="6"/><path d="M634 302 q10 -11 20 0"/>
      <path d="M706 373 v-20 h8 v9 h13 v11 z"/>
      <path d="M633 440 a11 11 0 0 1 22 0"/><line x1="630" y1="441" x2="658" y2="441"/>
    </g>
  </svg>
  <div class="industry-label" style="left:684px;top:141px">CHEMICAL INDUSTRY</div>
  <div class="industry-label" style="left:757px;top:213px">AUTOMOTIVE</div>
  <div class="industry-label" style="left:684px;top:284px">FOOD &amp; DRINKS</div>
  <div class="industry-label" style="left:757px;top:356px">MINING AND METALS</div>
  <div class="industry-label" style="left:684px;top:427px">ENERGY</div>

  <div class="social" style="top:518px"><i></i><i></i><i></i></div>
  <div class="page" style="top:514px">3</div>
</section>

<!-- Slide 4: who we are -->
<section class="slide" style="top:2052px">
  <div class="abs" style="left:516px;top:0;width:52px;height:563px;background:var(--blue)"></div>
  <div class="abs" role="img" aria-label="Glowing blue digital brain rising from a circuit chip on a dark background" style="left:516px;top:90px;width:484px;height:404px;background:radial-gradient(ellipse at 55% 48%,#1b6fd1 0%,#0b2f63 28%,#050b16 65%,#020408 100%)"></div>
  <div class="abs" style="left:0;top:442px;width:516px;height:52px;background:var(--red)"></div>
  <div class="brand">Quelmoro</div>

  <div class="dots"><i></i><i></i></div>
  <div class="heading">WHO WE ARE</div>
  <p class="who-copy" style="top:91px">We are specialists in automation, process control, information technologies, development and consulting for quality, efficiency and production. Our goal is to always provide the best solutions in conjunction with our technology partners Corvane.</p>
  <div class="who-sub" style="top:154px">Smart Machines</div>
  <p class="who-copy" style="top:196px">Intelligent machines in operation and control, in the same synchronization regardless of the brand installed. Efficiency that saves in operation. Creating brilliant machines.</p>
  <div class="who-sub" style="top:251px">Operational Excellence</div>
  <p class="who-copy" style="top:293px">Operational excellence is part of our language, strengthening the ties of efficiency in the company delivers revolutionary results. Saving and producing is easy with the experts.</p>
  <div class="who-sub" style="top:348px">Industrial Internet</div>
  <p class="who-copy" style="top:390px">Extending the Internet to industrial operation will exceed global energy savings by more than 1 Billion USD. A new generation of systems emerges, be part of this revolution.</p>

  <div class="social" style="top:518px"><i></i><i></i><i></i></div>
  <div class="page" style="top:514px">4</div>
</section>

<!-- Slide 5: tech allies -->
<section class="slide" style="top:2694px">
  <div class="dots"><i></i><i></i></div>
  <div class="heading">TECH ALIES</div>
  <div class="brand">Quelmoro</div>

  <div class="ally" style="left:52px;top:100px;width:146px;height:146px"><b></b>Corvane</div>
  <div class="ally" style="left:302px;top:106px;width:146px;height:146px">Lumabit</div>
  <div class="ally" style="left:172px;top:219px;width:146px;height:146px"><b></b>Talvex</div>
  <div class="ally" style="left:46px;top:331px;width:146px;height:146px">Linkroute</div>
  <div class="ally" style="left:295px;top:338px;width:146px;height:146px">Stellan</div>

  <div class="allies-copy">
    <p>The world is changing around us. Industrial enterprises need a technology partner that can help them survive—and thrive—wherever the situation, whatever the disruption. That's where Talvex shines.</p>
    <p>Our unique portfolio of CAD, PLM, IoT, and AR technologies—delivered on-prem, hybrid, and SaaS—creates a closed loop between the digital and physical worlds to transform how everything around us is engineered, manufactured, and serviced. This digital thread enables continuity of data across departments and fosters collaboration across functions, empowering the people who are involved at every step.</p>
    <p>Industry 4.0</p>
    <p>Industry 4.0 stands for the fourth major change in industrial production, which is achieved through comprehensive digitalisation. The focus is on the intelligent networking of processes and machines through modern communication and information technology. The overriding goals of Industry 4.0 are productivity increases, cost reductions and more flexible manufacturing.</p>
    <p>Cloud</p>
    <p>The manufacturing industry must meet increasing demands for faster delivery and higher production. Cloud technology is helping manufacturers meet these demands. By 2023, nearly half of the software used by manufacturers will be cloud-based. Now is the time to integrate the cloud into manufacturing to stay competitive.</p>
  </div>

  <div class="social" style="top:518px"><i></i><i></i><i></i></div>
  <div class="page" style="top:500px">5</div>
</section>

</body>
</html>
```